Sample Box for Collegiate Alumni Fundraising

We are a screen printing and embroidery company. Our core services are 1) printing & embroidery on apparel (t-shirts, hoodies etc) 2) promo products like mugs, stickers and 3) fulfillment (shipping orders to individuals that have placed orders.
I would like a sample box designed for our specific target market - College and university alumni giving offices. These offices are in charge of running fundraising campaigns. The two main types of campaigns are Giving Day (each school choses their own unique date but most are in the spring) and Lantern Crest (this is a set date each year which occurs the Tuesday after Thanksgiving). Many schools host their own day as well as participate in Lantern Crest. Oftentimes we are tasked with research and tracking down the right product for each campaign.
I have attached two examples that we had created for running clubs. I am open to both real photos or illustrations. I do not want to match these examples, I just want to demonstrate the general design of a sample box.
I do want to highlight our services on side panels like the examples. Printing, Fulfillment, Product Options

```html
<!DOCTYPE html>
<html lang="en">
<head>
<meta charset="utf-8">
<title>Alumni Giving Partnership – Sample Box Panels</title>
<link href="https://fonts.googleapis.com/css2?family=Libre+Baskerville:ital,wght@0,400;0,700;1,400&family=Montserrat:wght@500;600;700&display=swap" rel="stylesheet">
<style>
  :root{
    --navy:#1c3a78;
    --navy-deep:#142c5e;
    --orange:#d9663f;
    --orange-soft:#e07248;
    --cream:#f1ebe1;
    --white:#ffffff;
    --bg:#c9c9c9;
    --serif:"Libre Baskerville", Georgia, serif;
    --sans:"Montserrat", Arial, sans-serif;
  }
  *{box-sizing:border-box;margin:0;padding:0}
  html,body{width:1200px;height:1200px;overflow:hidden}
  body{background:var(--bg);position:relative;font-family:var(--sans)}
  .panel{position:absolute;overflow:hidden}

  /* brand lockup */
  .brand{display:flex;align-items:center;justify-content:center;gap:8px;font-family:var(--sans);font-weight:700;font-size:14px;letter-spacing:.12em}
  .brand-mark{width:14px;height:14px;background:var(--orange)}

  /* lid top */
  .lid-top{left:50px;top:70px;width:530px;height:480px}
  .lid-photo{position:absolute;inset:0;background:linear-gradient(175deg,#e6a55e 0%,#b8682f 35%,#5b3a24 70%,#2e241f 100%)}
  .lid-top .brand{position:absolute;top:48px;left:0;right:0;color:var(--white)}
  .lid-title{position:absolute;left:0;right:0;bottom:90px;text-align:center;color:var(--white)}
  .lid-kicker{font-family:var(--serif);font-size:17px;letter-spacing:.35em;margin-bottom:6px}
  .lid-heading{font-family:var(--serif);font-weight:700;font-size:84px;line-height:1}
  .lid-rule{display:flex;align-items:center;justify-content:center;gap:10px;margin-top:14px}
  .lid-rule span{display:block;width:150px;height:2px;background:var(--orange)}

  /* front panel */
  .front{left:50px;top:550px;width:530px;height:170px;background:var(--navy);display:flex;align-items:center;justify-content:space-around;padding:0 20px}
  .service{color:var(--white);font-weight:600;font-size:16px;letter-spacing:.1em;text-align:center;line-height:1.4;text-transform:uppercase}
  .divider{width:2px;height:56px;background:var(--orange)}

  /* inside lid */
  .inside-lid{left:620px;top:70px;width:530px;height:480px}
  .inside-photo{position:absolute;inset:0;background:linear-gradient(180deg,#f3eee6 0%,#ebe1cf 38%,#c9b48c 62%,#7c6a48 85%,#4f4a35 100%)}
  .inside-lid .brand{position:absolute;top:40px;left:0;right:0;color:var(--navy)}
  .inside-head{position:absolute;top:80px;left:0;right:0;text-align:center;color:var(--navy)}
  .inside-head h2{font-family:var(--serif);font-weight:700;font-size:44px}
  .inside-head p{font-size:14px;line-height:1.5;margin-top:8px;font-weight:500}

  /* inside base */
  .inside-base{left:620px;top:550px;width:530px;height:170px;background:var(--orange);display:flex;align-items:center;justify-content:center}
  .tagline{font-family:var(--serif);font-style:italic;color:var(--cream);font-size:26px;line-height:1.4;text-align:center}

  /* back panel */
  .kits{left:50px;top:760px;width:530px;height:370px;background:var(--navy)}
  .kits-copy{position:absolute;left:40px;bottom:60px;color:var(--white)}
  .kits-copy h3{font-weight:700;font-size:36px}
  .kits-copy p{font-size:15px;margin-top:10px;font-weight:500}
  .kits-photo{position:absolute;right:40px;top:40px;width:200px;height:190px;border-radius:6px;background:linear-gradient(160deg,#26468a,#152d60)}

  /* side panels */
  .side{top:760px;width:255px;height:370px;background:var(--navy);color:var(--white);padding:30px 24px}
  .side-fulfill{left:620px}
  .side-print{left:895px}
  .side h4{font-weight:700;font-size:22px;line-height:1.25}
  .side p{font-size:13px;line-height:1.5;margin-top:10px;font-weight:500}
  .side-photo{position:absolute;left:24px;right:24px;bottom:30px;height:150px;border-radius:6px}
  .side-fulfill .side-photo{background:linear-gradient(160deg,#c8a57a,#8a6a45)}
  .side-print .side-photo{background:linear-gradient(160deg,#2a4a8c,#132a5a)}
</style>
</head>
<body>

<section class="panel lid-top">
  <div class="lid-photo" role="img" aria-label="Crowd of alumni walking through a sunlit autumn campus with school pennants"></div>
  <div class="brand"><span class="brand-mark"></span>CEDAR HOLLOW GRAPHICS</div>
  <div class="lid-title">
    <p class="lid-kicker">ALUMNI GIVING</p>
    <h1 class="lid-heading">Partnership</h1>
    <div class="lid-rule">
      <span></span>
      <svg width="14" height="13" viewBox="0 0 14 13" aria-hidden="true"><path d="M7 12.5 1.2 6.8A3.3 3.3 0 0 1 7 2.3a3.3 3.3 0 0 1 5.8 4.5Z" fill="#d9663f"/></svg>
      <span></span>
    </div>
  </div>
</section>

<section class="panel front">
  <p class="service">Printing &amp;<br>Embroidery</p>
  <span class="divider"></span>
  <p class="service">Product<br>Options</p>
  <span class="divider"></span>
  <p class="service">Fulfillment<br>Made Easy</p>
</section>

<section class="panel inside-lid">
  <div class="inside-photo" role="img" aria-label="Historic columned campus hall at sunrise with trees, lamp post banner and students"></div>
  <div class="brand"><span class="brand-mark"></span>CEDAR HOLLOW GRAPHICS</div>
  <div class="inside-head">
    <h2>Giving Day Ready.</h2>
    <p>Custom merch, donor gifts &amp; fulfillment<br>for alumni offices &amp; advancement teams.</p>
  </div>
</section>

<section class="panel inside-base">
  <p class="tagline">You lead the campaign.<br>We handle the details.</p>
</section>

<section class="panel kits">
  <div class="kits-photo" role="img" aria-label="Navy alumni crewneck sweatshirt and matching cap"></div>
  <div class="kits-copy">
    <h3>Campaign Kits</h3>
    <p>Shipped directly to alumni supporters</p>
  </div>
</section>

<section class="panel side side-fulfill">
  <h4>Fulfillment<br>Made Easy</h4>
  <p>Packed &amp; shipped to individual supporters</p>
  <div class="side-photo" role="img" aria-label="Kraft gift pack tied with red ribbon and tag"></div>
</section>

<section class="panel side side-print">
  <h4>Printing<br>&amp; Embroidery</h4>
  <p>Custom apparel &amp; promo goods for every campaign</p>
  <div class="side-photo" role="img" aria-label="Embroidered navy cap"></div>
</section>

</body>
</html>
```